Professional, Elegant, Modern and Playful stationery design for an Orthodontist (Dentist)

We need a new stationery design for an Orthodontist (Dentist).
We would like to see designs that are elegant, but also playful. The designs and colors should be in harmony with the existing logo (uploaded).
The font of the logo text is roboto (Google), you don't need to use the same font, but the used font has to be in harmony with the font used in the logo and it has to be usable in Microsoft Word.
The colors used have to be in harmony with the logo.
The design for following parts are needed:
- A4 letter paper design
- A4 Microsoft Word Template (with and without letterhead)
- Envelope designs for C4 and C5 with the window on the right side
- CD/DVD-label design
- Stamping design

Target Market(s)

Orthodontist (Dentist)

Industry/Entity Type

It Professional

Font styles to use
Sans Serif

Colors

Designer to choose colors to be used in the design.

Requirements
Must have
• * Logo files are uploaded
• * A4 letter paper design: for printing press
• - Address position is on the right side
• - Needed Information in the letterhead:
• - Logo with company name as a unit
• or
• - separate the logo from the text and position them separately
• - Text needed:
• Kieferorthopädie Sonnhalde
• Dr. med. dent. Till Brösecke
• Fachzahnarzt für Kieferorthopädie (CH)
• Eidg. dipl. Zahnarzt, Mitglied VFP und BZR
• Wendelhofweg 7
• 8604 Talbach
• 044 518 27 40
• (fax:)
• 044 518 27 41
• info@zahnbogen-praxis.example
• www.zahnbogen-praxis.example
• * A4 Microsoft Word Templates:
• - an empty and undesigned text example template is uploaded
• - the address lines are already correctly positioned behind the envelope window
• - design the positions of all elements
• - choose suitable fonts, which are in harmony with the font in the logo and the letterhead and which can be used in Microsoft Word (compatible with latest version, no old versions (.doc) needed)
• - choose suitable font sizes weights and colors, which are in harmony with the font in the logo and the letterhead.
• - One version with letterhead for printing on an empty paper
• - One version without letterhead for printing on a paper with letterhead already printed in printing press
• * Envelopes C4 and C5
• - window on the right side
• - Logo with company name (see uploaded files) as a unit
• or
• - Text needed:
• Wendelhofweg 7
• 8604 Talbach
• * DVD/CD-label:
• or
• - Text needed:
• Wendelhofweg 7
• 8604 Talbach
• 044 518 27 40
• info@zahnbogen-praxis.example
• www.zahnbogen-praxis.example
• - Patient name with birth date:
• Doe John, *1.2.1999
• - Two lines of text describing the contents on the CD/DVD
• * Stamping design:
• - Logo
• - Text:
• Kieferorthopädie Sonnhalde GmbH
• Wendelhofweg 7
• 8604 Talbach
Should not have
• - Old Microsoft Word versions (.doc)

```html
<!DOCTYPE html>
<html lang="de">
<head>
<meta charset="utf-8">
<title>Kieferorthopädie Sonnhalde – Stationery</title>
<link rel="stylesheet" href="https://fonts.googleapis.com/css2?family=Open+Sans:wght@400;600;700&family=Arimo:wght@700&display=swap">
<style>
:root{
  --navy:#1f2a5c;
  --blue:#29a3dc;
  --paper:#f6f6f6;
  --white:#ffffff;
  --ground:#e3e4e6;
  --ink:#3a3a3a;
  --muted:#7a7f8f;
}
*{box-sizing:border-box;margin:0;padding:0}
html,body{width:1200px;height:720px;overflow:hidden;background:var(--ground)}
body{position:relative;font-family:"Open Sans",Arial,sans-serif;color:var(--ink)}
.label{position:absolute;font-family:Arimo,Arial,sans-serif;font-weight:700;font-size:13.5px;color:#4a4a4a;transform:translateX(-50%);white-space:nowrap}
.sheet{position:absolute;background:var(--paper);overflow:hidden}

/* brand unit: circle + name */
.brand{position:absolute;display:flex;align-items:flex-start;gap:4px}
.brand-dot{border-radius:50%;background:var(--navy);flex:none}
.brand-name{font-weight:700;color:var(--navy);line-height:1.15;white-space:nowrap}
.brand-sub{color:var(--muted);line-height:1.3;white-space:nowrap}

/* folder */
.folder{left:98px;top:99px;width:212px;height:288px;background:var(--white)}
.folder-band{position:absolute;left:0;top:118px;width:100%;height:7px;background:var(--blue)}
.folder-base{position:absolute;left:0;top:125px;width:100%;bottom:0;background:var(--navy)}
.folder-fold{position:absolute;left:164px;top:0;width:1px;height:100%;background:rgba(0,0,0,.08)}

/* letter */
.letter{left:351px;top:107px;width:194px;height:272px}
.sender{position:absolute;left:130px;top:8px;font-size:2.8px;line-height:1.45;color:#555;border-left:.5px solid #bbb;padding-left:3px;white-space:nowrap}
.letter-body{position:absolute;left:17px;top:68px;width:162px;font-size:3.6px;line-height:1.6;color:#555}
.letter-body p{margin-bottom:6px}
.signature{width:60px;height:14px;background:linear-gradient(90deg,rgba(40,40,40,.15),rgba(40,40,40,.05));margin:4px 0 3px}
.foot-bars{position:absolute;left:0;bottom:4px;width:100%;height:5px}
.foot-navy{position:absolute;left:0;top:0;width:58%;height:100%;background:var(--navy)}
.foot-blue{position:absolute;left:60%;right:0;top:0;height:100%;background:var(--blue);clip-path:polygon(4px 0,100% 0,100% 100%,0 100%)}

/* envelopes */
.env-back{position:absolute;background:var(--paper)}
.env-flap{position:absolute;left:0;top:0;width:100%;height:24px;background:var(--navy);border-radius:0 0 12px 12px}
.env-flap .brand-dot{position:absolute;left:50%;top:6px;width:10px;height:10px;margin-left:-5px;background:var(--white)}
.env-front .addr{position:absolute;font-size:3px;line-height:1.45;color:#555;white-space:nowrap}

/* stamp */
.stamp{position:absolute;left:213px;top:529px;width:114px;height:114px;border-radius:50%;background:var(--navy);color:var(--white);text-align:center}
.stamp-dot{position:absolute;left:50%;top:20px;width:34px;height:34px;margin-left:-17px;border-radius:50%;border:2px solid var(--white)}
.stamp-text{position:absolute;left:0;right:0;top:72px;font-size:3.6px;line-height:1.4}
.stamp-text b{font-size:5.4px;display:block}

/* cd */
.cd-cover{position:absolute;left:463px;top:476px;width:207px;height:189px;background:var(--navy);color:var(--white)}
.disc{position:absolute;left:702px;top:481px;width:182px;height:182px;border-radius:50%;background:var(--white);border:4px solid var(--navy);overflow:hidden;text-align:center}
.disc-wave{position:absolute;left:-4px;top:-4px;width:190px;height:40px}
.disc-dot{position:absolute;left:50%;top:8px;width:14px;height:14px;margin-left:-7px;border-radius:50%;background:var(--white)}
.disc-hole{position:absolute;left:50%;top:50%;width:54px;height:54px;margin:-27px 0 0 -27px;border-radius:50%;border:.6px solid #cfd6e0}
.disc-patient{position:absolute;left:0;right:0;top:40px;font-size:6.4px;line-height:1.25;color:var(--blue)}
.disc-brand{position:absolute;left:0;right:0;top:128px;font-size:3.8px;line-height:1.35;color:#666}
.disc-brand b{display:block;font-size:6px;color:var(--navy)}
</style>
</head>
<body>

<div class="label" style="left:201px;top:73px">Folder A4</div>
<div class="label" style="left:448px;top:75px">Letter Head A4</div>
<div class="label" style="left:703px;top:73px">Envelopes C5 Front - Back</div>
<div class="label" style="left:955px;top:73px">Envelopes C4 Front - Back</div>
<div class="label" style="left:641px;top:452px">CD/DVD with cover</div>
<div class="label" style="left:268px;top:513px">Stamp</div>

<!-- Folder -->
<section class="sheet folder" aria-label="Folder A4">
  <div class="brand" style="left:38px;top:59px">
    <span class="brand-dot" style="width:22px;height:22px"></span>
    <div>
      <div class="brand-name" style="font-size:7px">Kieferorthopädie Sonnhalde</div>
      <div class="brand-sub" style="font-size:5px">Dr. med. dent. Till Brösecke<br>Fachzahnarzt für Kieferorthopädie (CH)</div>
    </div>
  </div>
  <div class="folder-band"></div>
  <div class="folder-base"></div>
  <div class="folder-fold"></div>
</section>

<!-- Letterhead -->
<section class="sheet letter" aria-label="Letter Head A4">
  <div class="brand" style="left:17px;top:10px">
    <span class="brand-dot" style="width:11px;height:11px"></span>
    <div>
      <div class="brand-name" style="font-size:3.8px">Kieferorthopädie Sonnhalde</div>
      <div class="brand-sub" style="font-size:2.8px">Dr. med. dent. Till Brösecke<br>Fachzahnarzt für Kieferorthopädie (CH)</div>
    </div>
  </div>
  <div class="sender">Eidg. dipl. Zahnarzt,<br>Mitglied VFP und BZR<br>Wendelhofweg 7<br>8604 Talbach<br><br>044 518 27 40<br>044 518 27 41<br>info@zahnbogen-praxis.example<br>www.zahnbogen-praxis.example</div>
  <div class="letter-body">
    <p>Talbach, 30.3.2017</p>
    <p style="margin-top:12px">Subject</p>
    <p style="margin-top:8px">Sehr geehrte Damen und Herren</p>
    <p>Wir danken Ihnen für Ihr Vertrauen und freuen uns, Ihnen den weiteren Ablauf der Behandlung zu erläutern. Die nächsten Termine finden Sie in der Beilage. Bei Fragen stehen wir Ihnen jederzeit gerne zur Verfügung.</p>
    <p>Bitte bringen Sie zum nächsten Besuch die aktuelle Versichertenkarte sowie allfällige Röntgenbilder mit. Sollten Sie einen Termin verschieben müssen, melden Sie sich bitte mindestens zwei Tage im Voraus telefonisch bei uns.</p>
    <div class="signature" role="img" aria-label="Handwritten signature"></div>
    <div>Till Brösecke,<br>Dr. med. dent.,<br>Fachzahnarzt für Kieferorthopädie (CH)</div>
  </div>
  <div class="foot-bars"><div class="foot-navy"></div><div class="foot-blue"></div></div>
</section>

<!-- Envelope C5 -->
<div class="env-back" style="left:626px;top:101px;width:171px;height:245px" aria-label="Envelope C5 back">
  <div class="env-flap"><span class="brand-dot"></span></div>
</div>
<section class="sheet env-front" style="left:603px;top:135px;width:172px;height:243px" aria-label="Envelope C5 front">
  <div class="brand" style="left:18px;top:13px">
    <span class="brand-dot" style="width:10px;height:10px"></span>
    <div>
      <div class="brand-name" style="font-size:3.6px">Kieferorthopädie Sonnhalde</div>
      <div class="brand-sub" style="font-size:2.7px">Dr. med. dent. Till Brösecke<br>Fachzahnarzt für Kieferorthopädie (CH)</div>
    </div>
  </div>
  <div class="addr" style="left:126px;top:14px">Eidg. dipl. Zahnarzt,<br>Mitglied VFP und BZR<br>Wendelhofweg 7<br>8604 Talbach</div>
  <div class="foot-bars"><div class="foot-navy"></div><div class="foot-blue"></div></div>
</section>

<!-- Envelope C4 -->
<div class="env-back" style="left:880px;top:103px;width:151px;height:244px;border-top:1.5px solid var(--blue)" aria-label="Envelope C4 back">
  <div class="env-flap"><span class="brand-dot"></span></div>
</div>
<section class="sheet env-front" style="left:860px;top:143px;width:152px;height:235px" aria-label="Envelope C4 front">
  <div class="brand" style="left:16px;top:8px">
    <span class="brand-dot" style="width:10px;height:10px"></span>
    <div>
      <div class="brand-name" style="font-size:3.4px">Kieferorthopädie Sonnhalde</div>
      <div class="brand-sub" style="font-size:2.6px">Dr. med. dent. Till Brösecke<br>Fachzahnarzt für Kieferorthopädie (CH)</div>
    </div>
  </div>
  <div class="addr" style="left:111px;top:10px">Eidg. dipl. Zahnarzt,<br>Mitglied VFP und BZR<br>Wendelhofweg 7<br>8604 Talbach</div>
  <div class="foot-bars"><div class="foot-navy"></div><div class="foot-blue"></div></div>
</section>

<!-- Stamp -->
<section class="stamp" aria-label="Stamp">
  <span class="stamp-dot"></span>
  <div class="stamp-text"><b>Kieferorthopädie Sonnhalde</b>Dr. med. dent. Till Brösecke<br>Fachzahnarzt für Kieferorthopädie (CH)</div>
</section>

<!-- CD cover -->
<section class="cd-cover" aria-label="CD/DVD cover">
  <div class="brand" style="left:34px;top:82px">
    <span class="brand-dot" style="width:22px;height:22px;background:var(--white)"></span>
    <div class="brand-name" style="font-size:11px;color:var(--white);padding-top:4px">Kieferorthopädie<br>Sonnhalde</div>
  </div>
</section>

<!-- CD disc -->
<section class="disc" aria-label="CD/DVD label">
  <svg class="disc-wave" viewBox="0 0 190 40" preserveAspectRatio="none" aria-hidden="true">
    <path d="M0 0H190V30C160 22 130 16 95 30C60 42 30 38 0 30Z" fill="var(--navy)"/>
  </svg>
  <span class="disc-dot"></span>
  <div class="disc-hole"></div>
  <div class="disc-patient">Patient name &amp; birth date<br>Doe John, *1.2.1999</div>
  <div class="disc-brand"><b>Kieferorthopädie Sonnhalde</b>Dr. med. dent. Till Brösecke<br>Fachzahnarzt für Kieferorthopädie (CH)</div>
</section>

</body>
</html>
```